International non-profit org needs web design

A new non-profit global organization called The Worldwide Venture Bridge Council (WVC) needs a web design. The organization is a global community of professionals engaged in the commercialization aspects of innovation. The members of the community share experience and knowledge about exemplary practices and business models in order to continuoulsy improve the field of expertise.

Target Market(s)

governments, investors, universities, professionala

Industry/Entity Type

Non-Profit

Requirements
Must have
• landing page and capability to add tabs

```html
<!DOCTYPE html>
<html lang="en">
<head>
<meta charset="utf-8">
<title>The Worldwide Venture Bridge Council</title>
<link href="https://fonts.googleapis.com/css2?family=Didact+Gothic&family=PT+Sans:wght@400;700&display=swap" rel="stylesheet">
<style>
:root{
  --red:#e42a3a;
  --black:#0b0b0c;
  --white:#ffffff;
  --grey:#e6e6e6;
  --text:#222;
}
*{margin:0;padding:0;box-sizing:border-box}
html,body{width:855px;height:1200px;overflow:hidden;background:var(--white)}
body{font-family:"PT Sans",Arial,sans-serif;color:var(--text);position:relative}
.abs{position:absolute}
.nowrap{white-space:nowrap}
.heading{font-family:"Didact Gothic",Arial,sans-serif;color:var(--red);font-size:21px;font-weight:400;white-space:nowrap}

.topbar{left:0;top:0;width:855px;height:30px;background:var(--black)}
.topbar .event{left:20px;top:10px;font-size:10px;color:var(--red);white-space:nowrap}
.topbar .mail{left:659px;top:8px;font-size:12px;color:var(--red)}
.phone-tab{left:659px;top:26px;width:158px;height:22px;background:var(--black);border-radius:0 0 8px 8px;color:var(--white);font-size:13px;padding:1px 0 0 18px;word-spacing:4px;white-space:nowrap}

.brand{left:16px;top:56px;display:flex;align-items:center;gap:8px}
.brand-dot{width:32px;height:32px;border-radius:50%;background:var(--red)}
.brand-name{font-size:34px;font-weight:700;color:var(--red);letter-spacing:1px}

.login{left:468px;top:72px;font-size:13px;color:var(--red)}
.field{height:19px;background:var(--grey);font-size:11px;color:#b5b5b5;padding:2px 10px}
.go{left:809px;top:70px;width:27px;height:19px;background:var(--black);color:var(--white);border-radius:6px;font-size:12px;font-weight:700;text-align:center;line-height:19px}

.nav{left:200px;top:97px;width:655px;height:22px;background:var(--black)}
.nav-tab{left:10px;top:97px;width:190px;height:23px;background:var(--white)}
.menu-item{position:absolute;font-size:12.5px;color:var(--white);white-space:nowrap;line-height:22px;top:0}
.menu-item.sep{color:#ccc}
.redline{left:0;top:119px;width:855px;height:2px;background:var(--red)}

.hero{left:0;top:121px;width:855px;height:294px;background:linear-gradient(90deg,#c8101f 0%,#e5333f 35%,#ee5561 70%,#f47b85 100%)}
.hero-photo{left:60px;top:121px;width:320px;height:294px;background:linear-gradient(180deg,#c79a85 0%,#8a5a48 55%,#2a1d1a 100%);border-radius:140px 140px 0 0}
.hero-text{left:421px;top:221px;font-size:17px;line-height:21px;color:var(--white);white-space:nowrap}
.arrow{top:357px;width:22px;height:22px}

.welcome-text{left:25px;top:468px;font-size:11px;line-height:25.5px;color:var(--text);white-space:nowrap}
.step{left:562px;display:flex;align-items:center;gap:8px;white-space:nowrap}
.step-num{width:38px;height:36px;border-radius:7px;background:linear-gradient(180deg,#f0505d,#c41826);color:var(--white);font-size:15px;display:flex;align-items:center;justify-content:center;box-shadow:0 1px 2px #888}
.step-title{font-size:16px;color:#555;line-height:16px}
.step-sub{font-size:11.5px;color:#777;line-height:13px}

.dark{left:0;top:637px;width:855px;height:312px;background:var(--black)}
.divider{top:655px;width:1px;height:275px;background:#2b2b2b}
.objectives{left:20px;top:683px;list-style:none;color:var(--white);font-size:11px;line-height:13px;white-space:nowrap}
.objectives li{position:relative;padding-left:17px;margin-bottom:14px}
.objectives li::before{content:"";position:absolute;left:2px;top:3px;border-left:6px solid var(--red);border-top:3.5px solid transparent;border-bottom:3.5px solid transparent}
.value-photo{left:312px;top:681px;width:228px;height:102px;border-radius:6px;background:linear-gradient(180deg,#eef0f2 0%,#cfd3d8 55%,#3a3a40 100%)}
.value-text{left:310px;top:794px;color:var(--white);font-size:11px;line-height:13px;white-space:nowrap}
.value-text p{margin-bottom:14px}
.news{display:flex;align-items:center;gap:18px}
.date{width:56px;height:56px;border-radius:50%;background:radial-gradient(circle at 50% 40%,#d0202e,#7d0a14);border:3px solid #3a3a3a;color:var(--white);font-size:11.5px;line-height:14px;text-align:center;display:flex;flex-direction:column;justify-content:center}
.news-text{font-size:10px;line-height:12.5px;color:var(--white);white-space:nowrap}

.quote-mark{font-family:Georgia,serif;font-size:80px;color:#e3e3e3;line-height:1}
.avatar{width:58px;height:52px;background:linear-gradient(180deg,#d7b8a4,#8a6250)}
.testi{font-size:11px;line-height:20.5px;color:var(--text);white-space:nowrap}
.nl-label{font-size:12px;color:#444}
.nl-field{width:195px;height:22px;border:1px solid #ccc;background:var(--white)}
.subscribe{left:639px;top:1074px;width:100px;height:18px;border-radius:8px;background:linear-gradient(180deg,#555,#111);color:var(--white);font-size:12px;text-align:center;line-height:18px}

.footer{left:0;top:1126px;width:855px;height:32px;background:var(--black)}
.footer .menu-item{line-height:32px}
.footer-line{left:0;top:1158px;width:855px;height:3px;background:var(--red)}
.connect{left:684px;top:1133px;font-size:12px;color:var(--white);font-weight:700;white-space:nowrap}
.social{top:1133px;width:19px;height:19px;border-radius:50%;background:#2c5fa5;border:1px solid #9fb7d8}
.copyright{left:0;top:1167px;width:855px;text-align:center;font-size:12px;color:var(--text)}
</style>
</head>
<body>

<header>
  <div class="abs topbar">
    <div class="abs event">Dr. Elena Varga &nbsp;, The Crosswise Policy Forum , Northern Trade Mission, &nbsp;Halden, September 29, 2011</div>
    <div class="abs mail">elena.varga@bridge-council.org</div>
  </div>
  <div class="abs phone-tab">Cell : 555-310-4826</div>

  <div class="abs brand">
    <div class="brand-dot"></div>
    <div class="brand-name">WVC</div>
  </div>

  <div class="abs login">Login :</div>
  <div class="abs field" style="left:510px;top:70px;width:142px">Username</div>
  <div class="abs field" style="left:660px;top:70px;width:143px">Password</div>
  <div class="abs go">Go</div>

  <nav class="abs nav">
    <span class="menu-item" style="left:58px">Home</span>
    <span class="menu-item sep" style="left:115px">|</span>
    <span class="menu-item" style="left:146px">About Us</span>
    <span class="menu-item sep" style="left:218px">|</span>
    <span class="menu-item" style="left:246px">Services</span>
    <span class="menu-item sep" style="left:315px">|</span>
    <span class="menu-item" style="left:340px">Ideas</span>
    <span class="menu-item sep" style="left:389px">|</span>
    <span class="menu-item" style="left:418px">What we do?</span>
    <span class="menu-item sep" style="left:509px">|</span>
    <span class="menu-item" style="left:537px">Contact Us</span>
  </nav>
  <div class="abs nav-tab"></div>
  <div class="abs redline"></div>
</header>

<section>
  <div class="abs hero"></div>
  <div class="abs hero-photo" role="img" aria-label="Portrait photo of a smiling businesswoman"></div>
  <p class="abs hero-text">There are many variations of passages of Lorem Ipsum<br>available, but the majority have suffered alteration in<br>some form, by injected humour, or randomised words<br>which don't look even slightly believable.</p>
  <svg class="abs arrow" style="left:561px" viewBox="0 0 22 22"><circle cx="11" cy="11" r="10" fill="#9a9a9a" stroke="#ddd"/><path d="M15 9.5H10V7l-4 4 4 4v-2.5h5z" fill="#fff"/></svg>
  <svg class="abs arrow" style="left:596px" viewBox="0 0 22 22"><circle cx="11" cy="11" r="10" fill="#9a9a9a" stroke="#ddd"/><path d="M7 9.5h5V7l4 4-4 4v-2.5H7z" fill="#fff"/></svg>
</section>

<section>
  <h2 class="abs heading" style="left:25px;top:437px">Welcome to Our Website</h2>
  <p class="abs welcome-text">Lorem Ipsum is simply dummy text of the printing and typesetting industry. Lorem Ipsum has been the<br>industry's standard dummy text ever since the 1500s, when an unknown printer took a galley of type and<br>scrambled it to make a type specimen book. It has survived not only five centuries, but also the leap into<br>electronic typesetting, remaining essentially unchanged.There are many variations of passages of Lorem<br>Ipsum available, but the majority have suffered alteration in some form, by injected humour, or randomised<br>words which don't look even slightly believable.</p>

  <h2 class="abs heading" style="left:566px;top:437px">How it Works</h2>
  <div class="abs step" style="top:475px">
    <div class="step-num">01</div>
    <div><div class="step-title">Facilitate improvement of</div><div class="step-sub">Policies,Practices,Models and &nbsp;Evidence-based<br>success measurements</div></div>
  </div>
  <div class="abs step" style="top:531px">
    <div class="step-num">02</div>
    <div class="step-title">Used in commercialization</div>
  </div>
  <div class="abs step" style="top:586px">
    <div class="step-num">03</div>
    <div><div class="step-title">By sharing knowledge learned</div><div class="step-sub">from both successes and failures.</div></div>
  </div>
</section>

<section>
  <div class="abs dark"></div>
  <div class="abs divider" style="left:291px"></div>
  <div class="abs divider" style="left:563px"></div>

  <h2 class="abs heading" style="left:25px;top:648px">The Objectives</h2>
  <ul class="abs objectives">
    <li>Share exemplary practices in the commercialization<br>of research outcomes in our countries and regions</li>
    <li>Provide feedback on what is working and what is<br>not + the evidence-based methods of measure-<br>ments</li>
    <li>Promote international networking and partnerships<br>to create new multilateral or bilateral partnerships</li>
    <li>Communicate the impact of commercialization of<br>publicly funded research on our prosperity</li>
    <li>Work on &nbsp;global projects of common interest</li>
    <li>To gather on an annual basis to present and discuss<br>the successful practices, emerging models and<br>evidence-based measurement methods and deter-<br>mine how relevant they are universally.</li>
  </ul>

  <h2 class="abs heading" style="left:312px;top:648px">Value Proposition</h2>
  <div class="abs value-photo" role="img" aria-label="Photo of a smiling businessman and businesswoman in an office"></div>
  <div class="abs value-text">
    <p>Greater visibility in real time on new approaches to<br>commercialization</p>
    <p>A clear voice with strong arguments for influencing<br>policies on innovation, seeking new resources,<br>support and partners both internally within organi-<br>zations and domestically on a national level</p>
    <p>The opportunity to create partnerships and inter-<br>change talent</p>
  </div>

  <h2 class="abs heading" style="left:584px;top:648px">Lates News</h2>
  <div class="abs news" style="left:573px;top:689px">
    <div class="date">15th<br>Jun</div>
    <div class="news-text"><b>Lorem Ipsum is simply dummy text</b><br>&nbsp;of the printing and typesetting industry.<br>Lorem Ipsum has been the industry's<br>standard dummy text</div>
  </div>
  <div class="abs news" style="left:573px;top:772px">
    <div class="date">15th<br>Jun</div>
    <div class="news-text"><b>Lorem Ipsum is simply dummy text</b><br>&nbsp;of the printing and typesetting industry.<br>Lorem Ipsum has been the industry's<br>standard dummy text</div>
  </div>
  <div class="abs news" style="left:576px;top:854px">
    <div class="date">15th<br>Jun</div>
    <div class="news-text"><b>Lorem Ipsum is simply dummy text</b><br>&nbsp;of the printing and typesetting industry.<br>Lorem Ipsum has been the industry's<br>standard dummy text</div>
  </div>
</section>

<section>
  <div class="abs quote-mark" style="left:14px;top:958px">&ldquo;</div>
  <h2 class="abs heading" style="left:56px;top:970px">Testimonial</h2>
  <div class="abs avatar" style="left:26px;top:1008px" role="img" aria-label="Portrait photo of a client"></div>
  <p class="abs testi" style="left:90px;top:1002px">Lorem Ipsum is simply dummy<br>text of the printing and typeset-<br>ting industry. Lorem Ipsum has<br>been the industry's standard<br>dummy text</p>
  <div class="abs avatar" style="left:256px;top:1008px;width:60px;height:50px" role="img" aria-label="Portrait photo of a client"></div>
  <p class="abs testi" style="left:329px;top:1002px">Lorem Ipsum is simply dummy<br>text of the printing and typeset-<br>ting industry. Lorem Ipsum has<br>been the industry's standard<br>dummy text</p>
  <div class="abs quote-mark" style="left:448px;top:1058px">&rdquo;</div>

  <h2 class="abs heading" style="left:530px;top:970px">News Letter</h2>
  <div class="abs nl-label" style="left:540px;top:1016px">Name</div>
  <div class="abs nl-label" style="left:602px;top:1016px">:</div>
  <div class="abs nl-field" style="left:608px;top:1014px"></div>
  <div class="abs nl-label" style="left:540px;top:1041px">e-Mail</div>
  <div class="abs nl-label" style="left:602px;top:1041px">:</div>
  <div class="abs nl-field" style="left:608px;top:1039px"></div>
  <div class="abs subscribe">Subscribe</div>
</section>

<footer>
  <div class="abs footer">
    <span class="menu-item" style="left:69px">Home</span>
    <span class="menu-item sep" style="left:126px">|</span>
    <span class="menu-item" style="left:157px">About Us</span>
    <span class="menu-item sep" style="left:230px">|</span>
    <span class="menu-item" style="left:257px">Services</span>
    <span class="menu-item sep" style="left:326px">|</span>
    <span class="menu-item" style="left:350px">Ideas</span>
    <span class="menu-item sep" style="left:401px">|</span>
    <span class="menu-item" style="left:429px">What we do?</span>
    <span class="menu-item sep" style="left:521px">|</span>
    <span class="menu-item" style="left:548px">Contact Us</span>
  </div>
  <div class="abs connect">Connect with us</div>
  <div class="abs social" style="left:775px"></div>
  <div class="abs social" style="left:798px"></div>
  <div class="abs social" style="left:820px"></div>
  <div class="abs footer-line"></div>
  <div class="abs copyright">Copyright© 2011. www.wvc-council.org</div>
</footer>

</body>
</html>
```